3 x Professional Herbal Supplement Label Design Ready to Print in UK Standard + Example inc

Hi,
Thank you for taking the time to read. I'm looking for an excellent graphic designer experienced in creating supplement labels for our 3 new products. The labels should be sized and have the resolution ready for the printers.
Here is the work:
I'm looking for a new supplement label design that I can use for 3 new products called:
1 - Raspberry Ketone
2 - Garcinia Cambogia
3 - Green Coffee
You will only need to create a single label to enter the competition, as the label created will be the template for all 3 products listed above. You can choose whether you go for product 1, 2,or 3 to enter the design competition, but all 3 will be required on completion should you be selected.
Simply, the label template would be adjusted for the other products, what would be different is the product specifics like, name, background graphic of the ingredient and ingredients listed, directions of use, barcode etc.
The design I like, which I'd like you to copy and then artistically make different is attached and titled "BrightMeadow_Garcinia_Cambogia_LABEL.jpg"
My company logo is attached called "vorix final logo.ai" & "vorix-invis.png" - Please let me know if this resolution is not suitable.
The guidance information in designing a UK label from the supplement manufacturer is attached, as follows:
The supplement manufacturer has also provided a very basic example of a product they produced for another company (Not very good I know, but at least shows what goes where). Please do not use this as an example of a good design!
*** I will provide more specific product detail (ingredients, bar-code, dosage) if your initial design is liked and selected for adjustment, as we will require that all 3 label designs are completed.
*** The delivered image files will need to be in Photoshop format.

```html
<!DOCTYPE html>
<html lang="en">
<head>
<meta charset="utf-8">
<title>vorix supplement labels</title>
<link rel="stylesheet" href="https://fonts.googleapis.com/css2?family=Open+Sans:wdth,wght@75..100,400..800&display=swap">
<style>
:root{
  --canvas:#ececec;
  --label:#ffffff;
  --ink:#3a3a3a;
  --muted:#7a7a7a;
  --rule:#cfcfcf;
  --coffee:#2f8f3a;
  --coffee-soft:#7fb84a;
  --raspberry:#c42a43;
  --raspberry-soft:#e8607a;
  --garcinia:#e98d1b;
  --garcinia-soft:#f6c92a;
}
*{box-sizing:border-box;margin:0;padding:0}
html,body{width:1200px;height:709px;overflow:hidden}
body{background:var(--canvas);font-family:"Open Sans",Arial,sans-serif;color:var(--ink)}
.sheet{width:1200px;height:709px;display:flex;flex-direction:column;align-items:center;justify-content:center;gap:12px}
.label{position:relative;width:620px;height:215px;background:var(--label);border-radius:12px;box-shadow:0 2px 6px rgba(0,0,0,.18);overflow:hidden;isolation:isolate}
.label--coffee{--accent:var(--coffee);--accent-soft:var(--coffee-soft)}
.label--raspberry{--accent:var(--raspberry);--accent-soft:var(--raspberry-soft)}
.label--garcinia{--accent:var(--garcinia);--accent-soft:var(--garcinia-soft)}

.panel{position:absolute;top:16px;font-size:6.2px;line-height:1.45}
.panel--info{left:16px;width:138px}
.panel--use{left:482px;width:124px}
.panel h3{font-size:6.8px;font-weight:700;margin-bottom:2px}
.panel p{margin-bottom:4px}
.note{color:var(--accent);font-weight:700}
.facts{margin-top:18px;border:1px solid var(--ink);padding:3px 4px}
.facts h4{font-size:7.5px;font-weight:800;border-bottom:2px solid var(--ink);padding-bottom:1px}
.facts .serving{border-bottom:1px solid var(--rule);padding:1px 0}
.facts .row{display:flex;justify-content:space-between;border-bottom:1px solid var(--rule);padding:1px 0}
.facts .row:last-child{border-bottom:none}
.panel--use .brand{margin-top:26px;font-size:13px}
.panel--use .maker{color:var(--muted);text-align:right;margin-top:4px}

.produce{position:absolute;left:152px;top:8px;width:176px;height:199px;
  background:radial-gradient(closest-side,var(--accent-soft) 0%,var(--accent) 70%,rgba(255,255,255,0) 100%)}
.label--garcinia .produce{background:radial-gradient(closest-side,#ffd93a 0%,var(--garcinia-soft) 50%,#8c8a4a 82%,rgba(255,255,255,0) 100%)}

.title-block{position:absolute;left:300px;top:12px;width:180px}
.title-head{position:relative;height:28px}
.capsules{position:absolute;left:30px;top:0;font-size:6px;line-height:1.2;color:var(--accent)}
.brand{display:flex;align-items:center;gap:3px;font-weight:600;font-size:15px;color:var(--accent);line-height:1}
.title-head .brand{position:absolute;left:80px;top:10px}
.brand-dot{width:6px;height:6px;border-radius:50%;background:currentColor}
.product{margin-top:4px;background:var(--accent);color:#fff;font-stretch:78%;font-weight:700;font-size:20px;line-height:1.02;padding:5px 0 5px 70px;letter-spacing:.3px}
.formula{color:var(--accent);font-size:9px;line-height:1.15;text-align:right;padding-right:10px;margin-top:6px;font-stretch:85%}
.strength{background:var(--accent);color:#fff;font-size:9px;line-height:1.15;text-align:right;padding:3px 10px 3px 0;margin-top:4px;font-stretch:85%}
.claim{color:var(--accent);font-weight:700;font-size:9px;line-height:1.15;text-align:right;padding-right:10px;margin-top:6px;font-stretch:85%}
</style>
</head>
<body>
<main class="sheet">

  <article class="label label--coffee">
    <section class="panel panel--info">
      <h3>Ingredients</h3>
      <p>Green coffee bean extract, vegetable cellulose capsule, rice flour, magnesium stearate.</p>
      <p class="note">Food supplement. Keep out of reach of children.</p>
      <div class="facts">
        <h4>Supplement Facts</h4>
        <div class="serving">Serving size: 2 capsules</div>
        <div class="row"><span>Green Coffee Extract</span><span>400mg</span></div>
        <div class="row"><span>Chlorogenic Acid</span><span>200mg</span></div>
      </div>
    </section>
    <div class="produce" role="img" aria-label="Photo of green coffee cherries on a branch"></div>
    <section class="title-block">
      <div class="title-head">
        <p class="capsules">120<br>Vegetarian<br>Capsules</p>
        <p class="brand"><span class="brand-dot"></span>vorix</p>
      </div>
      <h2 class="product">GREEN<br>COFFEE</h2>
      <p class="formula">Advanced<br>Formula</p>
      <p class="strength">Maximum<br>Strength</p>
      <p class="claim">50%<br>CHLOROGENIC<br>ACID</p>
    </section>
    <section class="panel panel--use">
      <h3>Directions for Use</h3>
      <p>Take 2 capsules daily with water before meals. Do not exceed the stated dose.</p>
      <p class="note">Store in a cool dry place.</p>
      <p class="brand"><span class="brand-dot"></span>vorix</p>
      <p class="maker">Made in the UK</p>
    </section>
  </article>

  <article class="label label--raspberry">
    <section class="panel panel--info">
      <h3>Ingredients</h3>
      <p>Raspberry ketone extract, vegetable cellulose capsule, rice flour, magnesium stearate.</p>
      <p class="note">Food supplement. Keep out of reach of children.</p>
      <div class="facts">
        <h4>Supplement Facts</h4>
        <div class="serving">Serving size: 2 capsules</div>
        <div class="row"><span>Raspberry Ketone Extract</span><span>500mg</span></div>
        <div class="row"><span>Natural Ketones</span><span>100mg</span></div>
      </div>
    </section>
    <div class="produce" role="img" aria-label="Photo of ripe raspberries with a green leaf"></div>
    <section class="title-block">
      <div class="title-head">
        <p class="capsules">120<br>Vegetarian<br>Capsules</p>
        <p class="brand"><span class="brand-dot"></span>vorix</p>
      </div>
      <h2 class="product">RASPBERRY<br>KETONE</h2>
      <p class="formula">Advanced<br>Formula</p>
      <p class="strength">Maximum<br>Strength</p>
      <p class="claim">NATURAL<br>RASPBERRY<br>KETONES</p>
    </section>
    <section class="panel panel--use">
      <h3>Directions for Use</h3>
      <p>Take 2 capsules daily with water before meals. Do not exceed the stated dose.</p>
      <p class="note">Store in a cool dry place.</p>
      <p class="brand"><span class="brand-dot"></span>vorix</p>
      <p class="maker">Made in the UK</p>
    </section>
  </article>

  <article class="label label--garcinia">
    <section class="panel panel--info">
      <h3>Ingredients</h3>
      <p>Garcinia cambogia fruit extract, vegetable cellulose capsule, rice flour, magnesium stearate.</p>
      <p class="note">Food supplement. Keep out of reach of children.</p>
      <div class="facts">
        <h4>Supplement Facts</h4>
        <div class="serving">Serving size: 2 capsules</div>
        <div class="row"><span>Garcinia Fruit Extract</span><span>500mg</span></div>
        <div class="row"><span>Hydroxycitric Acid</span><span>300mg</span></div>
      </div>
    </section>
    <div class="produce" role="img" aria-label="Photo of whole and halved garcinia cambogia fruit"></div>
    <section class="title-block">
      <div class="title-head">
        <p class="capsules">120<br>Vegetarian<br>Capsules</p>
        <p class="brand"><span class="brand-dot"></span>vorix</p>
      </div>
      <h2 class="product">GARCINIA<br>CAMBOGIA</h2>
      <p class="formula">Advanced<br>Formula</p>
      <p class="strength">Maximum<br>Strength</p>
      <p class="claim">WHOLE<br>FRUIT<br>EXTRACT</p>
    </section>
    <section class="panel panel--use">
      <h3>Directions for Use</h3>
      <p>Take 2 capsules daily with water before meals. Do not exceed the stated dose.</p>
      <p class="note">Store in a cool dry place.</p>
      <p class="brand"><span class="brand-dot"></span>vorix</p>
      <p class="maker">Made in the UK</p>
    </section>
  </article>

</main>
</body>
</html>
```